Nutracuetical Company website. Selling 1 supplement product

I need a WordPress eCommerce site made for 1 product. We sell a probiotic with advanced technology. I want the site to be very informative with a health and wellness feel. Bright pictures with people smiling, etc... I need a separate page highlighting the lab test results

Currently on Vorbex https://www.vorbex.com/gp/product/K7QM2XR9TD

Target Market(s)

People with intestinal issues. IBS Chrons Irregularity

Industry/Entity Type

Health And Wellness

Number of Pages Required

4 page

Requirements
Must have
• I want the site to be very informative with a health and wellness feel. Bright pictures with people smiling, etc... I need a separate page highlighting the lab test results
Nice to have
• Colors should match the logo

```html
<!DOCTYPE html>
<html lang="en">
<head>
<meta charset="utf-8">
<title>Brightway Nutra</title>
<link href="https://fonts.googleapis.com/css2?family=Ubuntu:wght@400;500;700&family=Open+Sans:wght@400;600&display=swap" rel="stylesheet">
<style>
:root{
  --green:#7fb21e;
  --green-dark:#5e9410;
  --green-light:#a8d04a;
  --blue:#1a7cc9;
  --blue-dark:#0f5fa6;
  --text:#444;
  --muted:#777;
  --panel:#f6f6f6;
  --footer:#f1f1f1;
  --bar:#e4e4e4;
  --star:#6aa11a;
}
*{margin:0;padding:0;box-sizing:border-box}
html,body{width:731px;height:1200px;overflow:hidden;background:#fff}
body{position:relative;font-family:"Open Sans",sans-serif;color:var(--text)}
.abs{position:absolute}
.top-line{left:0;top:0;width:731px;height:3px;background:var(--green)}
.hero-bg{left:0;top:0;width:731px;height:400px;background:radial-gradient(ellipse at 40% 45%,#fff 0%,#f3f4f4 70%,#ececec 100%)}
.brand{left:99px;top:30px;font-family:"Ubuntu",sans-serif;font-weight:700;font-size:18px;color:var(--green);display:flex;align-items:center;gap:5px}
.brand .mark{width:12px;height:12px;border-radius:50%;background:var(--blue)}
.call{left:414px;top:9px;font-family:"Ubuntu",sans-serif;font-size:11px;color:#555}
.search{left:546px;top:8px;width:80px;height:15px;background:#fff;border:1px solid #e2e2e2;font-size:6px;color:#777;padding:3px 5px}
.search svg{position:absolute;right:5px;top:3px}
.nav{left:266px;top:38px;display:flex;align-items:center;gap:0;font-size:7px;color:#444}
.nav a{color:#444;text-decoration:none;padding:5px 6px;height:20px;display:flex;align-items:center}
.nav a.active{background:var(--blue);color:#fff;font-weight:600;width:40px;justify-content:center;margin-right:2px}
.cart{left:539px;top:38px;width:87px;height:19px;background:var(--green);color:#fff;font-size:6px;font-weight:600;display:flex;align-items:center;justify-content:center;gap:6px}
.hero-photo{left:96px;top:72px;width:306px;height:290px;border-radius:40% 40% 8px 8px;background:linear-gradient(180deg,#f1e2d8,#e7a8c6 55%,#7a6b77)}
.hero-drops{left:440px;top:80px;width:250px;height:300px;border-radius:50%;background:radial-gradient(ellipse,rgba(160,200,225,.35),rgba(190,215,170,.15) 60%,transparent 72%)}
.hero-title{left:411px;top:143px;font-family:"Ubuntu",sans-serif;font-size:13px;line-height:15px;color:var(--blue)}
.hero-title b{font-weight:700;color:var(--blue-dark)}
.hero-copy{left:414px;top:180px;width:210px;font-size:6px;line-height:10px;color:#333}
.btn-outline{left:414px;top:213px;width:80px;height:18px;border:1px solid var(--blue);background:#fff;color:#333;font-size:7px;font-weight:600;display:flex;align-items:center;justify-content:center}
.btn-buy{left:503px;top:213px;width:62px;height:18px;background:var(--blue);color:#fff;font-size:7px;font-weight:600;display:flex;align-items:center;justify-content:center}
.hero-price{left:414px;top:244px;font-family:"Ubuntu",sans-serif;font-size:23px;color:var(--green-dark)}
.stars{display:flex;gap:6px;color:var(--star);font-size:10px}
.hero-stars{left:416px;top:275px}
.hero-ship{left:417px;top:297px;font-size:7px;color:#555}
.arrow-dot{width:15px;height:15px;border-radius:50%;background:var(--blue);display:flex;align-items:center;justify-content:center}
.hero-arrows{left:579px;top:339px;display:flex;gap:7px}
.welcome-small{left:130px;top:420px;font-family:"Ubuntu",sans-serif;font-size:11px;color:#555}
.welcome-title{left:128px;top:435px;font-family:"Ubuntu",sans-serif;font-size:20px;color:var(--green-dark)}
.welcome-title b{font-weight:700}
.welcome-copy{left:130px;top:470px;width:291px;font-size:6px;line-height:13.6px;color:#444;text-align:justify}
.btn-read{left:130px;top:546px;width:62px;height:19px;background:var(--blue);color:#fff;font-size:7px;font-weight:600;display:flex;align-items:center;justify-content:center}
.bottles-photo{left:460px;top:416px;width:112px;height:128px;border-radius:12px;background:linear-gradient(180deg,#eef2f3,#cfe3b8 55%,#9ec6df)}
.athlete-photo{left:578px;top:456px;width:142px;height:156px;border-radius:50% 50% 0 0;background:linear-gradient(180deg,#3b2a24,#d9ab8d 35%,#c99377 80%,#e8e8e8)}
.products{left:0;top:612px;width:731px;height:426px;background:var(--panel)}
.products-title{left:0;top:627px;width:731px;text-align:center;font-family:"Ubuntu",sans-serif;font-size:19px;color:var(--green-dark)}
.card{width:134px;height:182px;top:668px;background:#fff;border:1px solid #e6e6e6;text-align:center}
.card .pic{position:absolute;left:37px;top:22px;width:60px;height:98px;border-radius:8px;background:linear-gradient(180deg,#e8eaec,#cfe4b5 55%,#a9cfe4)}
.card .pic.wide{left:26px;width:82px}
.card .cart-dot{position:absolute;right:9px;top:7px;width:26px;height:26px;border-radius:50%;background:var(--green-light);display:flex;align-items:center;justify-content:center}
.card .cart-dot.on{background:var(--green);border:2px solid #c5e08f}
.card .name{position:absolute;left:0;width:100%;top:127px;font-family:"Ubuntu",sans-serif;font-size:10px;color:var(--green-dark)}
.card .kind{position:absolute;left:0;width:100%;top:142px;font-size:5.5px;color:var(--green-dark)}
.card .price{position:absolute;left:0;width:100%;top:150px;font-family:"Ubuntu",sans-serif;font-weight:700;font-size:16px;color:var(--green-dark)}
.card .price.soft{color:#98c25a}
.reviews{top:856px;display:flex;align-items:center;gap:5px;font-size:6px;color:var(--green-dark)}
.reviews .stars{font-size:8px;gap:4px}
.prod-arrows{left:353px;top:884px;display:flex;gap:4px}
.prod-arrows .arrow-dot{width:10px;height:10px}
.scale-photo{left:16px;top:772px;width:98px;height:190px;border-radius:40% 40% 6px 6px;background:linear-gradient(180deg,#5a3a2a,#e5c0a5 25%,#f2f2f2 50%,#8a8f98)}
.partners-wave{left:0;top:895px}
.partners-title{left:530px;top:946px;font-family:"Ubuntu",sans-serif;font-size:18px;color:#fff}
.partner{top:985px;color:rgba(255,255,255,.75);font-family:"Ubuntu",sans-serif;font-weight:700;display:flex;align-items:center}
.footer{left:0;top:1038px;width:731px;height:138px;background:var(--footer)}
.f-head{top:1060px;font-size:6px;color:#444;text-transform:uppercase}
.f-links{left:116px;top:1078px;font-size:5.6px;line-height:13px;color:#444}
.email{left:226px;top:1074px;width:102px;height:17px;background:#fff;font-size:5px;color:#777;padding:5px 6px}
.subscribe{left:226px;top:1096px;width:57px;height:17px;background:var(--blue);color:#fff;font-size:6px;display:flex;align-items:center;justify-content:center}
.social{left:226px;top:1123px;display:flex;gap:3px}
.social span{width:15px;height:15px;border-radius:50%}
.map{left:373px;top:1061px;width:125px;height:83px;border:1px solid #ccc;background:linear-gradient(135deg,#eef0ea,#e2e6dc)}
.contact{left:518px;font-size:6.4px;color:#444;line-height:11px;display:flex;gap:8px}
.bottom-bar{left:0;top:1176px;width:731px;height:24px;background:var(--bar)}
.pay{top:1183px;left:130px;display:flex;gap:14px;font-size:5.5px;font-weight:600;color:#555}
.copy{left:454px;top:1185px;font-size:5px;color:#444}
</style>
</head>
<body>
<div class="abs hero-bg"></div>
<div class="abs top-line"></div>

<div class="abs hero-drops" role="img" aria-label="Soft water drops and leaf decoration"></div>

<div class="abs brand"><span class="mark"></span>Brightway Nutra</div>

<div class="abs call">
  <svg width="8" height="8" viewBox="0 0 24 24" style="vertical-align:-1px;margin-right:4px"><path fill="#ccc" d="M6.6 10.8a15 15 0 006.6 6.6l2.2-2.2c.3-.3.7-.4 1-.2 1.1.4 2.3.6 3.6.6.6 0 1 .4 1 1V20c0 .6-.4 1-1 1A17 17 0 013 4c0-.6.4-1 1-1h3.5c.6 0 1 .4 1 1 0 1.3.2 2.5.6 3.6.1.3 0 .7-.2 1L6.6 10.8z"/></svg>Call Us : 1800 - 555 0142
</div>
<div class="abs search">Search
  <svg width="8" height="8" viewBox="0 0 24 24"><circle cx="10" cy="10" r="6" fill="none" stroke="#555" stroke-width="2.5"/><path d="M15 15l6 6" stroke="#555" stroke-width="2.5"/></svg>
</div>

<nav class="abs nav">
  <a class="active">Home</a><a>About Us</a><a>Products</a><a>Blog</a><a>Testimonials</a><a>Contact Us</a>
</nav>
<div class="abs cart">
  <svg width="8" height="8" viewBox="0 0 24 24"><path fill="#fff" d="M2 3h3l3 11h11l3-8H7"/><circle cx="9" cy="19" r="2" fill="#fff"/><circle cx="18" cy="19" r="2" fill="#fff"/></svg>SHOPPING CART
</div>

<div class="abs hero-photo" role="img" aria-label="Smiling woman sitting cross-legged holding a dumbbell and a probiotic bottle"></div>

<svg class="abs" style="left:0;top:290px" width="731" height="110" viewBox="0 0 731 110">
  <path d="M0 40 C90 10 200 25 300 60 C420 100 560 95 731 70 L731 110 L0 110Z" fill="#fff"/>
  <path d="M0 40 C90 10 200 25 300 60 C420 100 560 95 700 72 C560 82 420 86 300 55 C200 30 90 28 0 55Z" fill="var(--green)"/>
</svg>

<div class="abs hero-title"><b>The Best Probiotic</b> - Improve<br>Digestion, Healthy Immune System...</div>
<div class="abs hero-copy">Leaky Gut, Chron's, IBS, Promotes Digestive Health FloraTek Two Step Acid Protection, Moneyback Guarantee, Brightway Nutra Probiotics</div>
<div class="abs btn-outline">LEARN MORE</div>
<div class="abs btn-buy">BUY NOW</div>
<div class="abs hero-price">$ 18.99</div>
<div class="abs stars hero-stars"><span>★</span><span>★</span><span>★</span><span>★</span><span>☆</span></div>
<div class="abs hero-ship">FREE Shipping on eligible orders</div>
<div class="abs hero-arrows">
  <span class="arrow-dot"><svg width="6" height="6" viewBox="0 0 10 10"><path d="M7 1L3 5l4 4" stroke="#fff" stroke-width="2" fill="none"/></svg></span>
  <span class="arrow-dot"><svg width="6" height="6" viewBox="0 0 10 10"><path d="M3 1l4 4-4 4" stroke="#fff" stroke-width="2" fill="none"/></svg></span>
</div>

<div class="abs welcome-small">Welcome</div>
<div class="abs welcome-title">Brightway <b>Nutra</b></div>
<p class="abs welcome-copy">Culpa qui officia deserunt mollitia animi, id est laborum et dolorum fuga. Et harum quidem rerum facilis est et expedita distinctio. Nam libero tempore, cum soluta nobis est eligendi optio cumque nihil impedit quo minus id quod maxime placeat facere possimus, omnis voluptas assumenda est, omnis dolor repellendus. Temporibus autem quibusdam et aut officiis debitis aut rerum necessitatibus saepe eveniet ut et voluptates</p>
<div class="abs btn-read">READ MORE</div>
<div class="abs bottles-photo" role="img" aria-label="Three probiotic supplement bottles"></div>
<div class="abs athlete-photo" role="img" aria-label="Fit woman lifting a kettlebell"></div>

<div class="abs products"></div>
<div class="abs products-title">Products</div>

<div class="abs card" style="left:136px">
  <div class="pic" role="img" aria-label="Probiotic bottle"></div>
  <span class="cart-dot on"><svg width="11" height="11" viewBox="0 0 24 24"><path fill="#fff" d="M2 3h3l3 11h11l3-8H7"/><circle cx="9" cy="19" r="2" fill="#fff"/><circle cx="18" cy="19" r="2" fill="#fff"/></svg></span>
  <div class="name">Probiotic - Nutra</div><div class="kind">supplements</div><div class="price">$18.99</div>
</div>
<div class="abs card" style="left:298px">
  <div class="pic" role="img" aria-label="Probiotic bottle, back label"></div>
  <span class="cart-dot"><svg width="11" height="11" viewBox="0 0 24 24"><path fill="#fff" d="M2 3h3l3 11h11l3-8H7"/><circle cx="9" cy="19" r="2" fill="#fff"/><circle cx="18" cy="19" r="2" fill="#fff"/></svg></span>
  <div class="name">Probiotic - Nutra</div><div class="kind">supplements</div><div class="price soft">$38.99</div>
</div>
<div class="abs card" style="left:459px">
  <div class="pic wide" role="img" aria-label="Three probiotic bottles"></div>
  <span class="cart-dot"><svg width="11" height="11" viewBox="0 0 24 24"><path fill="#fff" d="M2 3h3l3 11h11l3-8H7"/><circle cx="9" cy="19" r="2" fill="#fff"/><circle cx="18" cy="19" r="2" fill="#fff"/></svg></span>
  <div class="name">Probiotic - Nutra</div><div class="kind">supplements</div><div class="price soft">$28.99</div>
</div>

<div class="abs reviews" style="left:158px">Reviews : <span class="stars"><span>★</span><span>★</span><span>★</span><span>★</span><span>☆</span></span></div>
<div class="abs reviews" style="left:320px">Reviews : <span class="stars"><span>★</span><span>★</span><span>★</span><span>★</span><span>☆</span></span></div>
<div class="abs reviews" style="left:481px">Reviews : <span class="stars"><span>★</span><span>★</span><span>★</span><span>★</span><span>☆</span></span></div>
<div class="abs prod-arrows">
  <span class="arrow-dot"><svg width="5" height="5" viewBox="0 0 10 10"><path d="M7 1L3 5l4 4" stroke="#fff" stroke-width="2" fill="none"/></svg></span>
  <span class="arrow-dot"><svg width="5" height="5" viewBox="0 0 10 10"><path d="M3 1l4 4-4 4" stroke="#fff" stroke-width="2" fill="none"/></svg></span>
</div>

<svg class="abs partners-wave" width="731" height="143" viewBox="0 0 731 143">
  <path d="M0 55 C150 20 300 65 430 45 C560 25 650 5 731 30 L731 143 L0 143Z" fill="#d9d9d9"/>
  <path d="M0 70 C150 45 300 70 430 50 C560 30 650 12 731 40 L731 143 L0 143Z" fill="url(#g)"/>
  <defs><linearGradient id="g" x1="0" y1="0" x2="0" y2="1"><stop offset="0" stop-color="#9cc93a"/><stop offset="1" stop-color="#6ea21a"/></linearGradient></defs>
</svg>
<div class="abs scale-photo" role="img" aria-label="Smiling woman holding a bathroom scale and tape measure"></div>
<div class="abs partners-title">Partners</div>
<div class="abs partner" style="left:116px"><span style="width:30px;height:29px;border-radius:4px;background:rgba(255,255,255,.55)"></span></div>
<div class="abs partner" style="left:172px;top:992px;font-size:11px;letter-spacing:2px">HALDEN GROUP</div>
<div class="abs partner" style="left:338px"><span style="width:29px;height:29px;border-radius:50%;background:rgba(255,255,255,.55)"></span></div>
<div class="abs partner" style="left:398px;top:990px;font-size:14px;font-weight:500">Meridia Capital</div>
<div class="abs partner" style="left:533px;top:990px;font-size:11px">ACTIVE NATION</div>

<div class="abs footer"></div>
<div class="abs f-head" style="left:114px">Quick Links</div>
<div class="abs f-links">Home<br>About Us<br>Products<br>Testimonials<br>Blog<br>Contact Us</div>
<div class="abs f-head" style="left:226px">Connect</div>
<div class="abs email">Enter email id</div>
<div class="abs subscribe">SUBSCRIBE</div>
<div class="abs social"><span style="background:#2c4a8a"></span><span style="background:#2aa3e0"></span><span style="background:#d8343a"></span><span style="background:#b07a4e"></span></div>
<div class="abs map" role="img" aria-label="Street map showing the store location"></div>
<div class="abs f-head" style="left:518px">Contact Us</div>
<div class="abs contact" style="top:1078px">
  <svg width="7" height="9" viewBox="0 0 12 16"><path d="M6 0a6 6 0 00-6 6c0 4.5 6 10 6 10s6-5.5 6-10a6 6 0 00-6-6zm0 8.5A2.5 2.5 0 116 3.5a2.5 2.5 0 010 5z" fill="var(--blue)"/></svg>
  <span>Main Store 1420 Alder<br>Lane Fairview</span>
</div>
<div class="abs contact" style="top:1110px">
  <svg width="8" height="8" viewBox="0 0 24 24"><path fill="var(--blue)" d="M6.6 10.8a15 15 0 006.6 6.6l2.2-2.2c.3-.3.7-.4 1-.2 1.1.4 2.3.6 3.6.6.6 0 1 .4 1 1V20c0 .6-.4 1-1 1A17 17 0 013 4c0-.6.4-1 1-1h3.5c.6 0 1 .4 1 1 0 1.3.2 2.5.6 3.6.1.3 0 .7-.2 1L6.6 10.8z"/></svg>
  <span>(346)-555-0190</span>
</div>
<div class="abs contact" style="top:1126px">
  <svg width="8" height="7" viewBox="0 0 20 14"><rect width="20" height="14" rx="1" fill="var(--blue)"/><path d="M0 1l10 7 10-7" stroke="#fff" stroke-width="1.5" fill="none"/></svg>
  <span>info@brightwaynutra.com</span>
</div>

<div class="abs bottom-bar"></div>
<div class="abs pay"><span>Payvo</span><span>Cardix</span><span>Amtrex</span><span>Findra</span><span>Paylink</span></div>
<div class="abs copy">Copyrights © 2016, www.brightwaynutra.com. All Rights Reserved.</div>
</body>
</html>
```